Lumen Botanicals Label Project- Updates made to project!

Project Scope: Branding opportunity for internet based skin care line. Design coordinating label for 4 different products. Each design shall be editable in Adobe Illustrator as a template including all fonts, symbols, and guides. Submit a design for all 4 products (preferably together as it would look on a retail shelf), business card, and logo.
Cleanser: STEP 1 Label Size: 5 x 4.5 inches (w x h) CALM CLEANSER
Toner: STEP 2 Label Size: 5 x 4.5 inches (w x h) TRANQUIL TONER- A piece of each crystal sits at the bottom of each solution. It coordinates with the "Quiet Heart" of our logo.
Serum STEP 3 Label Size: Label Size: 4.25 x 2.25 ANTI-AGING SERUM
Moisturizer: STEP 4 Label Size: Label Size: 1”x7.25” MOISTURIZER
Each label needs to include:
Front:
Attractive larger sized STEP #
Logo
Product name and short description
Decorative design Symbol(s)
Back:
Area on back to say short description
Directions for use
Larger area for ingredients
Website: www.lumenbotanicals-example.com
Address of distribution
Barcode

Lumen Skin Care, an esthetician created line provides organic and natural based products for all skin types. With an emphasis on anti-aging, this simple 4- step system can be used by many including pregnant and oncology consumers. The unique thing about our line is that the toners and serums contain crystals such as amethyst and rose quarts to promote Quiet Heart as well as outer beauty. Each product is handmade with natural, quality ingredients and are 70-90% Organic.
Target Market: Women ages 30-45 years old. This demographic is on the go, and wants a simple-easy to read label, & a skin care system that addresses her concerns. Just as this consumer is mindful of her fitness and what she puts in her body, she tends to purchase environmentally friendly, and natural products. Health and wellness trends reflect this, as organic beauty products are expected to grow 74% from 2013 to 2018. She enjoys meditation and yoga, and she is curious about eastern medicine holistic healing trends.

Company Name: Lumen Skin Care
Tagline: Quiet Heart- Bright Face
Package Feel: Simple, elegant easy to read step on each product. STEP 1: AM/PM. Attractive numbering. A symbol that reflects the brand. Not necessarily a Jewel or Crystal because the name speaks for itself. Beautiful, soft, eye catching design that draws the consumer to pick it up. Clear or white label welcomed. Some color palettes provided.
Descriptive words the packaging should represent: Yoga, Zen, mystic, eye catching, healing energy, natural, quality ingredients, sophisticated, beautiful, serenity, easy to read- bold-attractive numbering on front.
Inspiration Brands: VARLA Organics- Beautiful watercolor packaging that resonates a "feeling"

Attached are pictures of the packaging, inspirational pictures, skin care lines that are attractive, ect.

Packaging SPECS:

Cleanser:
Color Clear
Size 4 oz
Material PET
Case Pack
Neck Finish 24-410
Diameter 1.58 in / 4.013 cm
Height 6 in / 15.240 cm
Label Dimensions 5x4.5
Print Dimensions 5x4.5
Print Dimensions in (diameter)

TONER BOTTLE: Same as above

SERUM BOTTLE:
Color Clear
Size 2 oz
Material PET
Neck Finish 20-410
Diameter 1.358 in / 3.449 cm
Height 3.274 in / 8.316 cm

Moisturizer:
2.3 oz
Height:53 mm
Diameter: 60 mm
Neck: 58/400

Target Market(s)

Women ages 30-45 years old. This demographic is on the go, and wants a simple-easy to read label, & a skin care system that addresses her concerns. Just as this consumer is mindful of her fitness and what she puts in her body, she tends to purchase environmentally friendly, and natural products. Health and wellness trends reflect this, as organic beauty products are expected to grow 74% from 2013 to 2018. She enjoys meditation and yoga, and she is curious about eastern medicine holistic healing trends.

Industry/Entity Type

Skin Care Product

Contact Information for Business Card

Details given upon completion.

Logo Text

Lumen Botanicals Quiet Heart- Bright Face

Requirements
Must have
• A large step number on the front. Coordinating symbols and colors. Must have a professional retail look and be easy to read.
Nice to have
• Clean, simple, eye catching packaging. Watercolor designs. Designs that inspire "feelings" www.varlaorganics-example.com

```html
<!DOCTYPE html>
<html lang="en">
<head>
<meta charset="utf-8">
<title>Lumen Skin Care – Label Set</title>
<link rel="stylesheet" href="https://fonts.googleapis.com/css2?family=Montserrat:wght@400;700;800&family=Raleway:wght@300;400&family=Roboto+Condensed:wght@400&display=swap">
<style>
  :root {
    --ink: #0a0a0a;
    --paper: #ffffff;
    --aqua-deep: #86e3ec;
    --aqua-mid: #b5eff4;
    --aqua-pale: #e3fbfd;
    --teal-line: #5fc9cf;
    --text-grey: #333333;
    --band-1: #b0b0b5;
    --band-2: #d7dade;
    --band-3: #f2f2f2;
    --band-4: #ede5de;
    --band-5: #ddd1c6;
  }
  * { box-sizing: border-box; margin: 0; padding: 0; }
  html, body { width: 1200px; height: 1200px; overflow: hidden; background: var(--paper); }
  .canvas { position: relative; width: 1200px; height: 1200px; }

  .label { position: absolute; overflow: hidden; text-align: center; color: var(--ink); }
  .label--cleanser { left: 54px; top: 32px; width: 525px; height: 582px; }
  .label--toner { left: 620px; top: 122px; width: 525px; height: 582px; }
  .label--serum { left: 186px; top: 642px; width: 262px; height: 494px; }

  .wash {
    position: absolute; inset: 0;
    background:
      radial-gradient(ellipse 60% 35% at 30% 18%, var(--aqua-deep), transparent 70%),
      radial-gradient(ellipse 55% 30% at 80% 25%, var(--aqua-mid), transparent 70%),
      radial-gradient(ellipse 70% 40% at 40% 75%, var(--aqua-mid), transparent 75%),
      linear-gradient(180deg, var(--aqua-mid) 0%, var(--aqua-pale) 60%, var(--aqua-pale) 100%);
  }

  .stripe { position: absolute; left: 0; right: 0; display: flex; height: 14px; }
  .stripe--top { top: 0; }
  .stripe--bottom { bottom: 0; height: 18px; }
  .stripe span:nth-child(1) { flex: 18; background: var(--band-1); }
  .stripe span:nth-child(2) { flex: 22; background: var(--band-2); }
  .stripe span:nth-child(3) { flex: 22.5; background: var(--band-3); }
  .stripe span:nth-child(4) { flex: 22; background: var(--band-4); }
  .stripe span:nth-child(5) { flex: 15.5; background: var(--band-5); }

  .brand-mark {
    position: absolute; left: 50%; top: 29px; width: 106px; height: 106px;
    margin-left: -53px; border: 3px solid var(--ink); border-radius: 50%;
  }
  .brand-name {
    position: absolute; left: 0; right: 0; top: 136px;
    font: 800 60px/1 "Montserrat", sans-serif; letter-spacing: 0.62em; padding-left: 0.62em;
  }
  .brand-sub {
    position: absolute; left: 0; right: 0; top: 196px;
    font: 800 22px/1 "Montserrat", sans-serif; letter-spacing: 0.14em;
  }

  .tagline-band {
    position: absolute; left: 0; right: 0; top: 232px; height: 68px;
    background: var(--ink); display: flex; align-items: center; justify-content: center; gap: 30px;
  }
  .tagline-band .dot { width: 52px; height: 52px; border: 2px solid var(--teal-line); border-radius: 50%; flex: none; }
  .tagline { color: var(--paper); font: 300 24px/1.2 "Raleway", sans-serif; text-align: center; }

  .info { position: absolute; left: 0; right: 0; top: 310px; font: 400 19px/1.3 "Raleway", sans-serif; letter-spacing: 0.06em; color: var(--text-grey); }

  .product-box { position: absolute; left: 102px; top: 372px; width: 323px; height: 121px; background: var(--ink); border: 3px solid var(--ink); }
  .product-name {
    position: relative; height: 76px; background: var(--paper);
    display: flex; align-items: center; justify-content: center;
    font: 800 24px/1 "Montserrat", sans-serif; letter-spacing: 0.14em;
  }
  .product-name::after {
    content: ""; position: absolute; left: 46%; bottom: -7px;
    border-left: 5px solid transparent; border-right: 5px solid transparent; border-top: 7px solid var(--paper);
  }
  .step-row { height: 39px; display: flex; align-items: center; justify-content: center; gap: 12px; color: var(--paper); }
  .step-label { font: 800 15px/1 "Montserrat", sans-serif; letter-spacing: 0.18em; }
  .step-numbers { font: 700 26px/1 "Montserrat", sans-serif; letter-spacing: 0.02em; }

  .claim { position: absolute; left: 0; right: 0; top: 502px; font: 400 17px/1 "Raleway", sans-serif; letter-spacing: 0.08em; color: var(--text-grey); }
  .volume { position: absolute; left: 0; right: 0; top: 530px; font: 400 22px/1 "Roboto Condensed", sans-serif; }

  /* small serum label */
  .label--serum .stripe { height: 11px; }
  .label--serum .stripe--bottom { height: 10px; }
  .label--serum .brand-mark { top: 64px; width: 68px; height: 68px; margin-left: -34px; border-width: 2px; }
  .label--serum .brand-name { top: 140px; font-size: 33px; }
  .label--serum .brand-sub { top: 172px; font-size: 14px; }
  .label--serum .tagline-band { top: 200px; height: 57px; gap: 18px; }
  .label--serum .tagline-band .dot { width: 38px; height: 38px; }
  .label--serum .tagline { font-size: 18px; }
  .label--serum .info { top: 318px; font-size: 13px; line-height: 1.2; }
  .label--serum .product-box { left: 26px; top: 358px; width: 217px; height: 81px; border-width: 2px; }
  .label--serum .product-name { height: 50px; font-size: 15px; letter-spacing: 0.12em; }
  .label--serum .product-name::after { bottom: -5px; border-left-width: 4px; border-right-width: 4px; border-top-width: 5px; }
  .label--serum .step-row { height: 27px; gap: 8px; }
  .label--serum .step-label { font-size: 10px; }
  .label--serum .step-numbers { font-size: 17px; }
  .label--serum .claim { top: 444px; font-size: 15px; }
  .label--serum .volume { top: 465px; font-size: 13px; }
</style>
</head>
<body>
<div class="canvas">

  <section class="label label--cleanser">
    <div class="wash" role="img" aria-label="Soft aqua watercolour wash"></div>
    <div class="stripe stripe--top"><span></span><span></span><span></span><span></span><span></span></div>
    <div class="brand-mark"></div>
    <div class="brand-name">LUMEN</div>
    <div class="brand-sub">skin care</div>
    <div class="tagline-band"><div class="dot"></div><p class="tagline">quiet heart<br>bright face</p></div>
    <p class="info">information line 1<br>information line 2</p>
    <div class="product-box">
      <div class="product-name">CALM CLEANSER</div>
      <div class="step-row"><span class="step-label">STEP</span><span class="step-numbers">01 02 03 04</span></div>
    </div>
    <p class="claim">natural based products</p>
    <p class="volume">00 oz</p>
    <div class="stripe stripe--bottom"><span></span><span></span><span></span><span></span><span></span></div>
  </section>

  <section class="label label--toner">
    <div class="wash" role="img" aria-label="Soft aqua watercolour wash"></div>
    <div class="stripe stripe--top"><span></span><span></span><span></span><span></span><span></span></div>
    <div class="brand-mark"></div>
    <div class="brand-name">LUMEN</div>
    <div class="brand-sub">skin care</div>
    <div class="tagline-band"><div class="dot"></div><p class="tagline">quiet heart<br>bright face</p></div>
    <p class="info">information line 1<br>information line 2</p>
    <div class="product-box">
      <div class="product-name">TRANQUIL TONER</div>
      <div class="step-row"><span class="step-label">STEP</span><span class="step-numbers">01 02 03 04</span></div>
    </div>
    <p class="claim">natural based products</p>
    <p class="volume">00 oz</p>
    <div class="stripe stripe--bottom"><span></span><span></span><span></span><span></span><span></span></div>
  </section>

  <section class="label label--serum">
    <div class="wash" role="img" aria-label="Soft aqua watercolour wash"></div>
    <div class="stripe stripe--top"><span></span><span></span><span></span><span></span><span></span></div>
    <div class="brand-mark"></div>
    <div class="brand-name">LUMEN</div>
    <div class="brand-sub">skin care</div>
    <div class="tagline-band"><div class="dot"></div><p class="tagline">quiet heart<br>bright face</p></div>
    <p class="info">information line 1<br>information line 2</p>
    <div class="product-box">
      <div class="product-name">ANTI-AGING SERUM</div>
      <div class="step-row"><span class="step-label">STEP</span><span class="step-numbers">01 02 03 04</span></div>
    </div>
    <p class="claim">natural based products</p>
    <p class="volume">00 oz</p>
    <div class="stripe stripe--bottom"><span></span><span></span><span></span><span></span><span></span></div>
  </section>

</div>
</body>
</html>
```